Music Festival in Colorado Needs Awesome Flier Design

We need an eye-catching & captivating flier design for an annual music festival in Denver, CO (USA). The festival features the best Colorado musicians within the genres of jam - funk - bluegrass - electronic - reggae - rock.

The design should look clean and professional while still being creative and unique. The past three years' flier designs are attached, as well as the logo and some other designs that match the aesthetic of what we're looking for.

This festival has a big element of Colorado pride so any

Target Market(s)

Hippies - live music enthusiasts - partiers. Ages 21 - 40.

Industry/Entity Type

Entertainment

Colors
0355a3
ec1f27
ffffff
fbed22

Requirements
Must have
• Attached design text.
Nice to have
• - Quality texture and psychedelic elements.
• - Colorado pride elements; color scheme (red, white, blue & yellow), flag, ect.
• - Nature elements are awesome but this is also a downtown festival so keep that in mind.
Should not have
• Cheesy artwork.

```html
<!DOCTYPE html>
<html lang="en">
<head>
<meta charset="utf-8">
<title>Pass the Sound – Colorado Music Festival Flier</title>
<link rel="stylesheet" href="https://fonts.googleapis.com/css2?family=Bebas+Neue&family=Oswald:wght@500;700&display=swap">
<style>
  :root {
    --backdrop: #686566;
    --paper: #ffffff;
    --festival-blue: #2c649c;
    --ink-blue: #1f4f8a;
    --night: #0b1726;
    --lineup-red: #ec1f27;
  }
  * { margin: 0; padding: 0; box-sizing: border-box; }
  html, body { width: 1200px; height: 1200px; overflow: hidden; }
  body { background: var(--backdrop); position: relative; }

  .flier {
    position: absolute; left: 218px; top: 18px;
    width: 764px; height: 1170px;
    background: var(--paper); overflow: hidden;
  }
  .flier__shapes { position: absolute; inset: 0; }

  .mountain-scene {
    position: absolute; left: 0; top: 170px; width: 764px; height: 400px;
  }

  .flier__text { position: absolute; left: 0; right: 0; text-align: center; }

  .edition {
    top: 28px; font-family: "Oswald", sans-serif; font-weight: 700;
    font-size: 30px; color: var(--festival-blue); letter-spacing: 1px;
  }
  .edition sup { font-size: 15px; }

  .festival-name__top {
    top: 100px; font-family: "Oswald", sans-serif; font-weight: 700;
    font-size: 42px; color: var(--paper); letter-spacing: 1px; line-height: 1;
  }
  .festival-name__main {
    top: 148px; font-family: "Bebas Neue", sans-serif;
    font-size: 184px; color: var(--paper); line-height: 1;
  }
  .festival-tag {
    position: absolute; left: 242px; top: 318px; width: 272px; height: 28px;
    background: var(--paper); border: 2px solid var(--night);
    font-family: "Oswald", sans-serif; font-weight: 500; font-size: 19px;
    color: var(--night); letter-spacing: 2.5px; text-align: center; line-height: 24px;
  }
  .dates {
    top: 372px; font-family: "Oswald", sans-serif; font-weight: 700;
    font-size: 36px; color: var(--paper); letter-spacing: 1px;
  }
  .dates sup { font-size: 17px; }
  .venue {
    top: 448px; font-family: "Oswald", sans-serif; font-weight: 500;
    font-size: 27px; color: var(--paper);
  }
  .address {
    top: 490px; font-family: "Oswald", sans-serif; font-weight: 500;
    font-size: 24px; color: var(--paper); letter-spacing: 0.5px;
  }
  .address sup { font-size: 12px; }

  .guitarist-art {
    position: absolute; left: 378px; top: 582px; width: 386px; height: 588px;
    background:
      radial-gradient(ellipse at 35% 18%, #e8262e 0%, #b0307a 35%, transparent 62%),
      linear-gradient(180deg, #c83a8a 0%, #f2e53a 42%, #8fd35a 72%, #1f8fd2 100%);
    border-radius: 46% 0 0 0;
    opacity: 0.9;
  }

  .lineup {
    position: absolute; left: 30px; width: 392px; top: 586px;
    list-style: none; text-align: center;
    font-family: "Oswald", sans-serif; font-weight: 700; font-size: 29px;
    line-height: 42px; letter-spacing: 2.5px; color: var(--lineup-red);
  }

  .tickets {
    position: absolute; left: 30px; width: 392px; top: 1108px; text-align: center;
    font-family: "Oswald", sans-serif; font-weight: 700; font-size: 17px;
    color: var(--ink-blue); letter-spacing: 1px;
  }
  .website {
    position: absolute; left: 30px; width: 392px; top: 1130px; text-align: center;
    font-family: "Oswald", sans-serif; font-weight: 700; font-size: 25px;
    color: var(--ink-blue); letter-spacing: 1px;
  }
</style>
</head>
<body>
  <main class="flier">
    <svg class="flier__shapes" width="764" height="1170" viewBox="0 0 764 1170" aria-hidden="true">
      <defs>
        <clipPath id="header-band">
          <path d="M0,0 H764 V454 Q382,654 0,454 Z"/>
        </clipPath>
      </defs>
      <path class="header-band" d="M0,0 H764 V454 Q382,654 0,454 Z" fill="var(--festival-blue)"/>
      <ellipse class="header-dome" cx="382" cy="0" rx="240" ry="82" fill="var(--paper)"/>
    </svg>

    <div class="mountain-scene" role="img" aria-label="Illustrated dark mountain range with pine trees across the blue header"
         style="clip-path: path('M0,284 Q382,484 764,284 V0 H0 Z');
                background: linear-gradient(180deg, rgba(11,23,38,0) 0%, rgba(11,23,38,0.35) 45%, rgba(11,23,38,0.6) 100%);"></div>

    <p class="flier__text edition">6<sup>TH</sup> ANNUAL</p>
    <h1>
      <span class="flier__text festival-name__top">PASS THE</span>
      <span class="flier__text festival-name__main">SOUND</span>
    </h1>
    <p class="festival-tag">COLORADO MUSIC FESTIVAL</p>
    <p class="flier__text dates">MAY 11<sup>TH</sup> – 13<sup>TH</sup>, 2018</p>
    <p class="flier__text venue">PINE STREET YARD</p>
    <p class="flier__text address">418 W. 52<sup>ND</sup> AVE DENVER, CO 80221</p>

    <div class="guitarist-art" role="img" aria-label="Illustration of a guitarist with flowing psychedelic red and purple hair playing an electric guitar"></div>

    <ul class="lineup">
      <li>REED CALLOWAY BAND,</li>
      <li>OPEN ROOM ORCHESTRA,</li>
      <li>SHIFT THEORY,</li>
      <li>THE COPPER SEEDS,</li>
      <li>J-RAE &amp; THE RIDGE,</li>
      <li>KESTREL,</li>
      <li>HELIX,</li>
      <li>SUMMIT ENSEMBLE,</li>
      <li>DUSKLIT, PARASONICS,</li>
      <li>PRISMATIC,</li>
      <li>CLEAR STATIC,</li>
      <li>RAIL YARD, ORBITS.</li>
    </ul>

    <p class="tickets">TICKETS &amp; MORE INFO @</p>
    <p class="website">WWW.PASSTHESOUNDFEST.COM</p>
  </main>
</body>
</html>
```